Postcard Design For House buying

I buy houses for cash that need a lot of repairs and need a post card that illustrate that, i would like one that is somehow cartoonish, I had an idea about a house and a man that was kicking to the house like you do with old cars and then he had some $ bills in his hand. This is just an idea and you should not limit yourself to that

Target Market(s)

Dallas TX (DFW)

Industry/Entity Type

Real Estate

Requirements
Must have
• A Text on the frot calling for action, like "Sell your house fast Call 512-740-3916"

```html
<!DOCTYPE html>
<html lang="en">
<head>
<meta charset="utf-8">
<title>Sell Your House Fast – Postcard</title>
<link href="https://fonts.googleapis.com/css2?family=Anton&family=Bebas+Neue&family=Oswald:wght@500;700&family=PT+Sans+Narrow:wght@400;700&family=PT+Sans:wght@700&display=swap" rel="stylesheet">
<style>
  :root {
    --page: #ecebe8;
    --red: #ec1c24;
    --yellow: #fff200;
    --white: #ffffff;
    --black: #0c0c0c;
    --panel: #f1f1f1;
    --blue: #1f80b8;
    --text-red: #d4141c;
    --line: #b9b9b9;
    --photo-a: #9fb0c4;
    --photo-b: #d8c9b4;
    --photo-c: #6f8f5a;
  }
  * { box-sizing: border-box; margin: 0; padding: 0; }
  html, body {
    width: 940px; height: 1200px; overflow: hidden;
    background: var(--page);
  }
  .card {
    position: absolute;
    box-shadow: 0 4px 14px rgba(0,0,0,.18);
    overflow: hidden;
  }
  /* Front */
  .card-front { left: 110px; top: 50px; width: 665px; height: 514px; background: var(--white); }
  .front-red { position: absolute; inset: 0; }
  .front-photo {
    position: absolute; inset: 0;
    background: linear-gradient(160deg, var(--photo-a) 0%, var(--photo-b) 45%, #c9a88e 65%, var(--photo-c) 100%);
    clip-path: polygon(392px 0, 665px 0, 665px 514px, 392px 514px, 318px 118px);
  }
  .kicker {
    position: absolute; left: 21px; top: 28px;
    font: 400 31px/1 "Bebas Neue", "Oswald", sans-serif;
    color: var(--yellow); letter-spacing: .5px;
  }
  .headline {
    position: absolute; left: 21px; top: 84px;
    font: 400 46px/1 "Bebas Neue", sans-serif;
    color: var(--white); letter-spacing: -.5px;
  }
  .cash {
    position: absolute; left: 20px; top: 130px;
    font: 400 82px/1 "Anton", sans-serif;
    color: var(--black); letter-spacing: 1px;
    text-shadow: 0 0 1px var(--white);
  }
  .cash .bang { font-size: 128px; position: relative; top: 8px; margin-left: 2px; }
  .front-list {
    position: absolute; left: 30px; top: 254px; list-style: none;
    font: 400 18px/25.7px "PT Sans Narrow", sans-serif; color: var(--white);
    text-transform: uppercase;
  }
  .front-list li { display: flex; align-items: center; gap: 6px; }
  .front-list svg { width: 16px; height: 16px; flex: none; }
  .call-btn {
    position: absolute; left: 29px; top: 438px; width: 314px; height: 48px;
    background: var(--black); border-radius: 9px; border: 1px solid var(--white);
    display: flex; align-items: center; justify-content: center; gap: 14px;
    font: 700 22px/1 "PT Sans Narrow", sans-serif; color: var(--white);
  }
  .call-btn svg, .call-row svg { width: 22px; height: 22px; }

  /* Back */
  .card-back { left: 149px; top: 596px; width: 667px; height: 516px; background: var(--white); }
  .back-panel { position: absolute; left: 0; top: 0; width: 365px; height: 516px; background: var(--panel); }
  .back-title {
    position: absolute; left: 15px; top: 26px;
    font: 700 35px/31px "Oswald", sans-serif; color: var(--blue); text-transform: uppercase;
  }
  .ribbon { position: absolute; left: 14px; top: 98px; width: 166px; height: 20px; }
  .ribbon-text {
    position: absolute; left: 20px; top: 101px;
    font: 400 9px/14px "PT Sans Narrow", sans-serif; color: #333;
  }
  .back-house {
    position: absolute; left: 202px; top: 12px; width: 185px; height: 131px;
    background: radial-gradient(ellipse at 50% 55%, #d7d2cc 0%, #b8735a 45%, rgba(241,241,241,0) 72%);
  }
  .back-list {
    position: absolute; left: 26px; top: 157px; list-style: none;
    font: 700 15px/25px "PT Sans Narrow", sans-serif; color: var(--text-red);
  }
  .back-list li { display: flex; align-items: center; gap: 9px; }
  .back-list svg { width: 10px; height: 10px; flex: none; }
  .back-note {
    position: absolute; left: 0; width: 365px; top: 344px; text-align: center;
    font: 700 13.5px/21px "PT Sans Narrow", sans-serif; color: var(--blue); text-transform: uppercase;
  }
  .call-row {
    position: absolute; left: 0; width: 365px; top: 394px;
    display: flex; justify-content: center; align-items: center; gap: 12px;
    font: 700 23px/1 "PT Sans Narrow", sans-serif; color: var(--blue);
  }
  .sell-btn {
    position: absolute; left: 26px; top: 439px; width: 313px; height: 48px;
    background: var(--black); border-radius: 9px;
    display: flex; align-items: center; justify-content: center;
    font: 400 32px/1 "Bebas Neue", sans-serif; color: var(--white); letter-spacing: .5px;
  }
  .stamp { position: absolute; left: 541px; top: 26px; width: 98px; height: 75px; border: 1px solid var(--line); }
  .address-line { position: absolute; left: 395px; width: 244px; height: 1px; background: var(--line); }
</style>
</head>
<body>

<section class="card card-front">
  <svg class="front-red" width="665" height="514" viewBox="0 0 665 514" aria-hidden="true">
    <polygon points="0,0 372,0 300,118 378,514 0,514" fill="var(--red)"/>
  </svg>
  <div class="front-photo" role="img" aria-label="Hand holding a small model house with dollar bills flying around"></div>

  <p class="kicker">Sell Your House Fast</p>
  <h1 class="headline">We Buy Houses</h1>
  <p class="cash">CA$H<span class="bang">!</span></p>

  <ul class="front-list">
    <li><svg viewBox="0 0 16 16"><rect x="1.5" y="2.5" width="12" height="12" fill="none" stroke="#111" stroke-width="1.6"/><path d="M4 8l3 3 7-9" fill="none" stroke="#111" stroke-width="2"/></svg>Distressed Properties</li>
    <li><svg viewBox="0 0 16 16"><rect x="1.5" y="2.5" width="12" height="12" fill="none" stroke="#111" stroke-width="1.6"/><path d="M4 8l3 3 7-9" fill="none" stroke="#111" stroke-width="2"/></svg>Inherited Properties</li>
    <li><svg viewBox="0 0 16 16"><rect x="1.5" y="2.5" width="12" height="12" fill="none" stroke="#111" stroke-width="1.6"/><path d="M4 8l3 3 7-9" fill="none" stroke="#111" stroke-width="2"/></svg>Short Sales</li>
    <li><svg viewBox="0 0 16 16"><rect x="1.5" y="2.5" width="12" height="12" fill="none" stroke="#111" stroke-width="1.6"/><path d="M4 8l3 3 7-9" fill="none" stroke="#111" stroke-width="2"/></svg>Divorced Situations</li>
    <li><svg viewBox="0 0 16 16"><rect x="1.5" y="2.5" width="12" height="12" fill="none" stroke="#111" stroke-width="1.6"/><path d="M4 8l3 3 7-9" fill="none" stroke="#111" stroke-width="2"/></svg>Any Condition-No Repairs Needed</li>
    <li><svg viewBox="0 0 16 16"><rect x="1.5" y="2.5" width="12" height="12" fill="none" stroke="#111" stroke-width="1.6"/><path d="M4 8l3 3 7-9" fill="none" stroke="#111" stroke-width="2"/></svg>No Commissions To Be Paid</li>
  </ul>

  <div class="call-btn">
    <span>Call Now</span>
    <svg viewBox="0 0 24 24" aria-hidden="true"><circle cx="12" cy="12" r="10.5" fill="none" stroke="#fff" stroke-width="1.8"/><path d="M8.3 6.5c.6-.4 1.2-.2 1.5.4l1 2c.2.5.1 1-.3 1.3l-.7.6c.6 1.3 1.6 2.4 2.9 3l.6-.7c.3-.4.9-.5 1.3-.3l2 1c.6.3.8.9.4 1.5-.7 1.1-1.8 1.6-3 1.2-3.1-1-5.5-3.4-6.5-6.5-.4-1.2.1-2.3.8-2.5z" fill="#fff"/></svg>
    <span>512-740-3916</span>
  </div>
</section>

<section class="card card-back">
  <div class="back-panel"></div>
  <h2 class="back-title">We Buy<br>Houses</h2>
  <svg class="ribbon" viewBox="0 0 166 20" aria-hidden="true">
    <polygon points="0,0 150,0 166,10 150,20 0,20 6,10" fill="#d9d9d9"/>
    <polygon points="0,0 150,0 166,10 6,10" fill="#e6e6e6"/>
  </svg>
  <p class="ribbon-text">Any Condition, Any Situation, Any Problem</p>
  <div class="back-house" role="img" aria-label="Illustrated house with a sold sign and stacks of cash"></div>

  <ul class="back-list">
    <li><svg viewBox="0 0 10 10"><path d="M1 5l3 3 5-7" fill="none" stroke="#222" stroke-width="1.6"/></svg>We Pay Cash For Your Property</li>
    <li><svg viewBox="0 0 10 10"><path d="M1 5l3 3 5-7" fill="none" stroke="#222" stroke-width="1.6"/></svg>We pay the closing costs</li>
    <li><svg viewBox="0 0 10 10"><path d="M1 5l3 3 5-7" fill="none" stroke="#222" stroke-width="1.6"/></svg>We buy the properties in AS IS condition</li>
    <li><svg viewBox="0 0 10 10"><path d="M1 5l3 3 5-7" fill="none" stroke="#222" stroke-width="1.6"/></svg>No repairs are needed before we buy.</li>
    <li><svg viewBox="0 0 10 10"><path d="M1 5l3 3 5-7" fill="none" stroke="#222" stroke-width="1.6"/></svg>No worries about financed offers falling through</li>
    <li><svg viewBox="0 0 10 10"><path d="M1 5l3 3 5-7" fill="none" stroke="#222" stroke-width="1.6"/></svg>Generally we can close in under 30 days</li>
  </ul>

  <p class="back-note">Selling your property in any condition<br>has never been easier!</p>

  <div class="call-row">
    <span>Call Now</span>
    <svg viewBox="0 0 24 24" aria-hidden="true"><circle cx="12" cy="12" r="10.5" fill="none" stroke="var(--blue)" stroke-width="1.8"/><path d="M8.3 6.5c.6-.4 1.2-.2 1.5.4l1 2c.2.5.1 1-.3 1.3l-.7.6c.6 1.3 1.6 2.4 2.9 3l.6-.7c.3-.4.9-.5 1.3-.3l2 1c.6.3.8.9.4 1.5-.7 1.1-1.8 1.6-3 1.2-3.1-1-5.5-3.4-6.5-6.5-.4-1.2.1-2.3.8-2.5z" fill="var(--blue)"/></svg>
    <span>512-740-3916</span>
  </div>

  <div class="sell-btn">Sell Your House Fast</div>

  <div class="stamp"></div>
  <div class="address-line" style="top:247px"></div>
  <div class="address-line" style="top:295px"></div>
  <div class="address-line" style="top:344px"></div>
  <div class="address-line" style="top:391px"></div>
</section>

</body>
</html>
```